Digital menu Skydiving company

Design Digital menu/pricelist for our company. It can have dynamic components. We are also looking for a Graphic design for all our projects. Our main goals are to look clean/sharp and professional. Information is in psd file

3 packages Violet Plunge, Meadow Journey, And Lantern Voyage. then we have addons and merchandise

Colors
0293ce
34a7d8
ffffff
fbee3f
3377b5
000000
f37122
ec1f27
e34197

Requirements
Must have
• Sorry If I couldn't get my vision across better, Please see really rough design idea attached. one large picture section that rotates through 3 or 4 pictures. then all the information down the bottom and on right (see menu pricelist attached)

```html
<!DOCTYPE html>
<html lang="en">
<head>
<meta charset="utf-8">
<title>Packages &amp; Pricing</title>
<link rel="stylesheet" href="https://fonts.googleapis.com/css2?family=Montserrat:wght@300;400;700;800&family=Open+Sans:wght@800&display=swap">
<style>
  :root {
    --page-bg: #e2e3e5;
    --panel-bg: #f0f0f0;
    --white: #ffffff;
    --sky-blue: #3fb0e3;
    --navy: #2b3590;
    --royal: #3178d2;
    --tagline: #34a7d8;
    --ink: #2b2b2b;
    --muted: #4a4a4a;
    --rule: #9a9a9a;
  }
  * { margin: 0; padding: 0; box-sizing: border-box; }
  html, body { width: 1200px; height: 803px; overflow: hidden; }
  body { background: var(--page-bg); position: relative; font-family: "Montserrat", sans-serif; }

  .menu-board {
    position: absolute; left: 28px; top: 80px;
    width: 1732px; height: 975px;
    transform: scale(0.66); transform-origin: top left;
    background: var(--white);
  }

  .hero-photo {
    position: absolute; left: 0; top: 0; width: 1269px; height: 496px;
    background: linear-gradient(180deg, #2353b0 0%, #3a78cc 45%, #86b4e4 68%, #6d7fa6 76%, #8a6a70 88%, #5a5a86 100%);
  }
  .hero-title {
    position: absolute; left: 0; width: 1269px; top: 374px;
    text-align: center; color: var(--white);
    font-family: "Open Sans", sans-serif; font-weight: 800; font-size: 90px; line-height: 1;
    letter-spacing: 1px; text-shadow: 0 3px 8px rgba(0,0,0,0.35);
  }
  .merch-photo {
    position: absolute; left: 1269px; top: 0; width: 463px; height: 496px;
    background: radial-gradient(ellipse at 55% 55%, #9cbbe0 0%, #d8dee6 45%, #efefef 75%);
  }

  .packages {
    position: absolute; left: 0; top: 514px; width: 1282px; height: 461px;
    background: var(--panel-bg);
  }
  .canyon-photo {
    position: absolute; left: 1282px; top: 514px; width: 450px; height: 461px;
    background: linear-gradient(170deg, #9aa4b2 0%, #c3cbd4 22%, #8f7e78 42%, #9a6e5a 62%, #6f5a52 82%, #55504e 100%);
  }

  .divider { position: absolute; top: 36px; width: 2px; height: 383px; background: #8c8c8c; }
  .divider--a { left: 422px; }
  .divider--b { left: 845px; }

  .package-title {
    position: absolute; top: 35px; width: 364px; height: 65px;
    color: var(--white); text-align: center;
    font-weight: 800; font-size: 24px; line-height: 28px; padding-top: 5px;
    text-transform: uppercase;
  }
  .package-title--violet { left: 29px; background: var(--sky-blue); }
  .package-title--meadow { left: 452px; background: var(--navy); }
  .package-title--lantern { left: 876px; background: var(--royal); }

  .tagline {
    position: absolute; top: 127px; color: var(--tagline);
    font-weight: 400; font-size: 20px; text-transform: uppercase; white-space: nowrap;
  }

  .features { list-style: none; position: absolute; }
  .features li {
    position: relative; padding-left: 21px;
    font-weight: 800; font-size: 17px; line-height: 17px; color: var(--ink);
    text-transform: uppercase;
  }
  .features svg { position: absolute; left: 0; top: 1px; width: 14px; height: 14px; }
  .features--violet { left: 29px; top: 182px; }
  .features--violet li { margin-bottom: 7px; }
  .features--meadow { left: 457px; top: 182px; }
  .features--meadow li { margin-bottom: 17px; padding-left: 26px; }
  .features--lantern { left: 874px; top: 182px; width: 403px; }
  .features--lantern li { margin-bottom: 17px; padding-left: 26px; }

  .addon-price { position: absolute; right: 43px; bottom: 0; }
  .leader { position: absolute; right: 0; bottom: -3px; height: 1px; background: var(--rule); }

  .merch-list { list-style: none; position: absolute; left: 29px; top: 246px; width: 360px; }
  .merch-list li {
    display: flex; align-items: baseline;
    font-weight: 300; font-size: 19px; line-height: 23.5px; color: var(--muted);
  }
  .merch-list .leader-fill { flex: 1; border-bottom: 1px solid var(--rule); margin: 0 6px 0 2px; }

  .price-tab {
    position: absolute; top: 409px; width: 196px; height: 52px;
    border-radius: 44px 44px 0 0; color: var(--white); text-align: center;
    font-weight: 800; font-size: 32px; line-height: 52px;
    box-shadow: 0 -1px 4px rgba(0,0,0,0.08);
  }
  .price-tab--violet { left: 110px; background: var(--sky-blue); }
  .price-tab--meadow { left: 537px; background: var(--navy); }
  .price-tab--lantern { left: 963px; background: var(--royal); }
</style>
</head>
<body>
<main class="menu-board">
  <section class="hero-photo" role="img" aria-label="Tandem skydivers in free fall over a canyon under a deep blue sky">
    <h1 class="hero-title">PACKAGES &amp; PRICING</h1>
  </section>
  <div class="merch-photo" role="img" aria-label="Merchandise: blue t-shirts, black hoodie, skydiving goggles and sneakers"></div>

  <section class="packages">
    <div class="divider divider--a"></div>
    <div class="divider divider--b"></div>

    <h2 class="package-title package-title--violet">Violet Plunge<br>16,000FT</h2>
    <h2 class="package-title package-title--meadow">Meadow Journey<br>16,000FT</h2>
    <h2 class="package-title package-title--lantern">Lantern Voyage<br>16,000FT</h2>

    <p class="tagline" style="left:35px">The skydive is naked, not you...</p>
    <p class="tagline" style="left:452px">Skydive &amp; share the memories...</p>
    <p class="tagline" style="left:919px">For the thrill seeker...</p>

    <ul class="features features--violet">
      <li><svg viewBox="0 0 14 14"><circle cx="7" cy="7" r="7" fill="#34a7d8"/><path d="M5.5 4l3 3-3 3" stroke="#fff" stroke-width="2" fill="none"/></svg>Tandem skydive from 16,000ft MSL</li>
      <li><svg viewBox="0 0 14 14"><circle cx="7" cy="7" r="7" fill="#34a7d8"/><path d="M5.5 4l3 3-3 3" stroke="#fff" stroke-width="2" fill="none"/></svg>Certificate of achievement</li>
    </ul>

    <ul class="merch-list">
      <li>T-Shirt Short Sleeve<span class="leader-fill"></span>$20</li>
      <li>T-Shirt Long Sleeve<span class="leader-fill"></span>$28</li>
      <li>Sweat Shirts<span class="leader-fill"></span>$30</li>
      <li>Hoodies<span class="leader-fill"></span>$38</li>
      <li>Goggles from<span class="leader-fill"></span>$12</li>
    </ul>

    <ul class="features features--meadow">
      <li><svg viewBox="0 0 14 14"><circle cx="7" cy="7" r="7" fill="#2b2b2b"/><path d="M5.5 4l3 3-3 3" stroke="#fff" stroke-width="2" fill="none"/></svg>Tandem skydive from<br>16,000ft MSL</li>
      <li><svg viewBox="0 0 14 14"><circle cx="7" cy="7" r="7" fill="#2b2b2b"/><path d="M5.5 4l3 3-3 3" stroke="#fff" stroke-width="2" fill="none"/></svg>Photos</li>
      <li><svg viewBox="0 0 14 14"><circle cx="7" cy="7" r="7" fill="#2b2b2b"/><path d="M5.5 4l3 3-3 3" stroke="#fff" stroke-width="2" fill="none"/></svg>Videos</li>
      <li><svg viewBox="0 0 14 14"><circle cx="7" cy="7" r="7" fill="#2b2b2b"/><path d="M5.5 4l3 3-3 3" stroke="#fff" stroke-width="2" fill="none"/></svg>Certificate of achievement</li>
    </ul>

    <ul class="features features--lantern">
      <li><svg viewBox="0 0 14 14"><circle cx="7" cy="7" r="7" fill="#0293ce"/><path d="M5.5 4l3 3-3 3" stroke="#fff" stroke-width="2" fill="none"/></svg>Tandem skydive from<br>16,000ft MSL<span class="addon-price">$319</span><span class="leader" style="left:241px"></span></li>
      <li><svg viewBox="0 0 14 14"><circle cx="7" cy="7" r="7" fill="#0293ce"/><path d="M5.5 4l3 3-3 3" stroke="#fff" stroke-width="2" fill="none"/></svg>Photos<span class="addon-price">$99</span><span class="leader" style="left:186px"></span></li>
      <li><svg viewBox="0 0 14 14"><circle cx="7" cy="7" r="7" fill="#0293ce"/><path d="M5.5 4l3 3-3 3" stroke="#fff" stroke-width="2" fill="none"/></svg>Videos<span class="addon-price">$99</span><span class="leader" style="left:186px"></span></li>
      <li><svg viewBox="0 0 14 14"><circle cx="7" cy="7" r="7" fill="#0293ce"/><path d="M5.5 4l3 3-3 3" stroke="#fff" stroke-width="2" fill="none"/></svg>Extreme extras<span class="addon-price">$50</span><span class="leader" style="left:276px"></span></li>
      <li><svg viewBox="0 0 14 14"><circle cx="7" cy="7" r="7" fill="#0293ce"/><path d="M5.5 4l3 3-3 3" stroke="#fff" stroke-width="2" fill="none"/></svg>Aerolith Skydive t-shirt</li>
      <li><svg viewBox="0 0 14 14"><circle cx="7" cy="7" r="7" fill="#0293ce"/><path d="M5.5 4l3 3-3 3" stroke="#fff" stroke-width="2" fill="none"/></svg>Certificate of achievement</li>
    </ul>

    <div class="price-tab price-tab--violet">$329</div>
    <div class="price-tab price-tab--meadow">$459</div>
    <div class="price-tab price-tab--lantern">$499</div>
  </section>

  <div class="canyon-photo" role="img" aria-label="View from an aircraft wing strut over a vast canyon landscape"></div>
</main>
</body>
</html>
```